US Recruiting Firm Needs Dynamic Tri-Fold Brochure

Need tri-fold professional brochure for HR recruiting and consulting firm based in the US.

Target Market(s)

Clients seeking administrative and human resources talent

Industry/Entity Type

Recruitment

Font styles to use
Sans Serif

Requirements
Should not have
• No weird shapes
• No heavy geometric shapes -- I prefer curvy lines
• Not a dark brochure

```html
<!DOCTYPE html>
<html lang="en">
<head>
<meta charset="utf-8">
<title>Piedmont Talent Partners – Tri-Fold Brochure</title>
<link href="https://fonts.googleapis.com/css2?family=Open+Sans:ital,wght@0,300;0,400;0,600;0,700;1,400;1,600&display=swap" rel="stylesheet">
<style>
  :root {
    --navy: #274a6b;
    --navy-deep: #1f3d59;
    --green: #8cc63f;
    --ink: #4d5560;
    --paper: #ffffff;
    --stage: #eceef1;
    --on-navy: #e8eef4;
    --photo-a: #9aa6b2;
    --photo-b: #d5dbe1;
  }
  * { margin: 0; padding: 0; box-sizing: border-box; }
  html, body { width: 1200px; height: 801px; overflow: hidden; }
  body {
    background: var(--stage);
    font-family: "Open Sans", Arial, sans-serif;
    color: var(--ink);
    display: flex; align-items: center; justify-content: center;
  }
  .brochure {
    width: 1050px; height: 760px;
    display: grid; grid-template-columns: repeat(3, 1fr);
    box-shadow: 0 10px 30px rgba(30, 45, 60, .18);
  }
  .panel { position: relative; overflow: hidden; }
  .panel--light { background: var(--paper); }
  .panel--navy { background: var(--navy); color: var(--on-navy); }

  .corner-frame {
    position: absolute; width: 120px; height: 120px; border: 0 solid var(--green);
  }
  .corner-frame--top-left { top: 18px; left: 18px; border-top-width: 7px; border-left-width: 7px; }
  .corner-frame--bottom-right { bottom: 22px; right: 18px; border-bottom-width: 7px; border-right-width: 7px; height: 230px; }

  .photo {
    position: absolute; left: 0; right: 0;
    background: linear-gradient(135deg, var(--photo-b), var(--photo-a));
  }
  .photo--about { bottom: 0; height: 250px; background: linear-gradient(160deg, #c7cfd6, #8d98a3 60%, #6f7b86); }
  .photo--team { top: 0; height: 255px; background: linear-gradient(200deg, #e9edf0, #a9b3bc 55%, #7d8892); }

  .about { padding: 44px 34px 0 40px; }
  .panel-title {
    font-weight: 700; font-size: 17px; letter-spacing: .3px; text-transform: uppercase;
    color: var(--navy); margin-bottom: 14px;
  }
  .body-copy { font-size: 11.2px; line-height: 1.55; text-align: justify; margin-bottom: 12px; }

  .partner { padding: 44px 32px 0 34px; }
  .partner .panel-title { color: #fff; font-size: 18px; margin-bottom: 12px; }
  .lead { font-weight: 700; font-size: 13px; line-height: 1.4; color: #fff; margin-bottom: 8px; }
  .partner .body-copy { text-align: left; font-size: 11.5px; }
  .statement {
    font-weight: 300; font-size: 16px; text-transform: uppercase; text-align: center;
    line-height: 1.3; margin: 8px 0 56px; color: #dde6ee;
  }
  .section-title {
    color: var(--green); font-weight: 700; font-size: 17px; text-transform: uppercase; margin-bottom: 12px;
  }
  .benefits { list-style: none; font-size: 11.8px; line-height: 1.45; margin-bottom: 70px; }
  .benefits li { position: relative; padding-left: 18px; margin-bottom: 10px; }
  .benefits li::before {
    content: ""; position: absolute; left: 2px; top: 6px; width: 6px; height: 6px;
    border-radius: 50%; background: #fff;
  }
  .mission .body-copy { text-align: justify; }

  .hr { padding: 278px 34px 0 34px; }
  .hr .panel-title { font-size: 18px; margin-bottom: 2px; }
  .kicker { font-style: italic; font-size: 12px; text-transform: uppercase; color: var(--navy); margin-bottom: 12px; }
  .qa { font-weight: 700; font-size: 12.5px; color: var(--navy); line-height: 1.4; margin-bottom: 10px; }
  .hr .body-copy { padding-right: 14px; }
</style>
</head>
<body>
  <main class="brochure">
    <section class="panel panel--light">
      <div class="corner-frame corner-frame--top-left"></div>
      <div class="about">
        <h2 class="panel-title">About Us</h2>
        <p class="body-copy">Piedmont Talent Partners is a recruiting and search firm that specializes in providing top-notch administrative, professional, and executive level human resources talent. We provide best-in-class talent to companies seeking to simplify their recruiting process, increase efficiency, and optimize productivity. Each search is customized based on our client's requirements. We provide quality, timely, and efficient services. Our recruiters are highly skilled in identifying, screening, interviewing, and assessing candidates across various industries. We develop a partnership with our client and candidate in order to make the recruitment process a success for both parties.</p>
        <p class="body-copy">At Piedmont Talent Partners, competence + talent emerge. We are experienced human resources professionals exclusively dedicated to recruiting and placing human resources professionals. We do we love and know for sure: human resources recruiting and consulting. We help awesome companies attract and retain the best employees, increase their profits, and optimize productivity.</p>
      </div>
      <div class="photo photo--about" role="img" aria-label="Photo of a smiling professional woman in an office with colleagues behind her"></div>
    </section>

    <section class="panel panel--navy">
      <div class="partner">
        <h2 class="panel-title">A Trusted Recruiting Partner</h2>
        <p class="lead">We have over 20 years of recruiting and human resources experience.</p>
        <p class="body-copy">Our recruiters have the expertise, insights, and passion to bring value-added recruiting services to your company.</p>
        <p class="statement">We have a track record of excellence.</p>
        <h3 class="section-title">Why Choose Us?</h3>
        <ul class="benefits">
          <li>We are HR experts dedicated to recruiting HR professionals</li>
          <li>Highly Qualified talent network</li>
          <li>Comprehensive pre-screening</li>
          <li>Simplified recruiting process</li>
          <li>Reasonable placement fees</li>
          <li>90-Day replacement guarantee</li>
        </ul>
        <div class="mission">
          <h3 class="section-title">Our Mission</h3>
          <p class="body-copy">We have a two-fold mission. We help companies hire the best HR staff to help meet organizational goals and cultivate a highly engaged, productive workforce. We also help HR talent find fulfilling work and careers with awesome companies.</p>
        </div>
      </div>
    </section>

    <section class="panel panel--light">
      <div class="photo photo--team" role="img" aria-label="Photo of business people shaking hands around a meeting table"></div>
      <div class="corner-frame corner-frame--bottom-right"></div>
      <div class="hr">
        <h2 class="panel-title">Human Resources</h2>
        <p class="kicker">One of the most critical function in a company</p>
        <p class="qa">Question: How do companies attract and retain the best employees?</p>
        <p class="qa">Answer: They so by hiring the best human resources staff.</p>
        <p class="body-copy">Human resources professionals are no longer paper pushers. They are now true business partners. They provide critical services that have direct impact on your company's bottom line. HR can help or hinder your company's progress. By hiring the best HR talent, your company is positioned and destined for success. Whether you need a HR Coordinator to assist with organizing and tracking projects, a HR Manager to be an advisory resource and provide both strategic and tactical solutions for managers and employees, or an executive to direct and lead the HR function, we can help.</p>
      </div>
    </section>
  </main>
</body>
</html>
```